The Calm of Orchards New Book Cover Design Project

Book cover design . Paperback, ebook, and Vocara (derived from book cover) files/images required.
Book Title: The Calm of Orchards
Subtitle: Fewer Rusty Gates
Author: Dorian Halvey
Files: Ebook, Paperback (Brellix & Tolvent Press), Vocara sized image
File size & information to be provided once design is ready. Brellix paperback will be 5.25 x 8.
Completion date is flexible. Planning to publish in November.
Updates

Need extra days to review

Target Market(s)

Motorcycle owners

Font styles to use
Sans Serif

Requirements
Must have
• A generic looking motorcycle (samples attached). Thumbnail easily recognized as a motorcycle book.
Nice to have
• Open to all ideas but am favoring my idea: to emphasize the title lettering similar to (but not a copy of) other Calm books (examples attached), on a plain background. All books in the category have a motorcycle on the cover. Author name and subtitle do not have to be prominent. Rider optional..
Should not have
• Should not look like a biker romance or fantasy cover or look cartoonish. Motorcycle pic should be fairly generic (brand, style,).

```html
<!DOCTYPE html>
<html lang="en">
<head>
<meta charset="utf-8">
<title>The Calm of Orchards — Dorian Halvey</title>
<link rel="stylesheet" href="https://fonts.googleapis.com/css2?family=Playfair+Display:wght@400;700;900&family=Cormorant+Garamond:wght@500&display=swap">
<style>
  :root {
    --paper: #ffffff;
    --ink: #0c0c0c;
    --accent: #e8242b;
    --chrome-light: #d9d9d9;
    --chrome-dark: #1a1a1a;
  }
  html, body {
    margin: 0;
    padding: 0;
    width: 840px;
    height: 1200px;
    overflow: hidden;
    background: var(--paper);
  }
  .cover {
    display: block;
    width: 840px;
    height: 1200px;
    background: var(--paper);
  }
  .title-hero {
    font-family: "Playfair Display", Georgia, serif;
    font-weight: 400;
    fill: var(--ink);
  }
  .title-small {
    font-family: "Playfair Display", Georgia, serif;
    font-weight: 400;
    fill: var(--ink);
    letter-spacing: 1px;
  }
  .title-accent {
    font-family: "Playfair Display", Georgia, serif;
    font-weight: 900;
    fill: var(--accent);
    letter-spacing: -2px;
  }
  .subtitle {
    font-family: "Cormorant Garamond", Georgia, serif;
    font-weight: 500;
    fill: var(--ink);
    letter-spacing: 2px;
  }
  .author {
    font-family: "Cormorant Garamond", Georgia, serif;
    font-weight: 500;
    fill: var(--ink);
    letter-spacing: 5px;
  }
</style>
</head>
<body>
<svg class="cover" viewBox="0 0 840 1200" xmlns="http://www.w3.org/2000/svg" aria-labelledby="cover-title">
  <title id="cover-title">The Calm of Orchards: Fewer Rusty Gates, by Dorian Halvey</title>
  <defs>
    <radialGradient id="bike-tones" cx="50%" cy="50%" r="55%">
      <stop offset="0%" stop-color="var(--chrome-light)"/>
      <stop offset="45%" stop-color="#6e6e6e"/>
      <stop offset="100%" stop-color="var(--chrome-dark)"/>
    </radialGradient>
    <radialGradient id="bike-fade" cx="50%" cy="50%" r="50%">
      <stop offset="0%" stop-color="#000" stop-opacity="0"/>
      <stop offset="100%" stop-color="#fff" stop-opacity="1"/>
    </radialGradient>
  </defs>

  <g class="title-block">
    <text class="title-small" x="352" y="262" font-size="34">THE</text>
    <text class="title-hero" x="56" y="490" font-size="430">C</text>
    <text class="title-hero" x="352" y="490" font-size="250">alm</text>
    <text class="title-small" x="356" y="532" font-size="30">OF</text>
    <text class="title-accent" x="304" y="590" font-size="64">ORCHARDS</text>
  </g>

  <text class="subtitle" x="360" y="640" font-size="30">Fewer Rusty Gates</text>

  <g class="cover-photo" role="img" aria-label="Photograph of a classic black café-style motorcycle with chrome exhaust and round headlight, three-quarter front view on white">
    <ellipse cx="430" cy="850" rx="190" ry="160" fill="url(#bike-tones)"/>
    <ellipse cx="430" cy="850" rx="195" ry="165" fill="url(#bike-fade)"/>
  </g>

  <text class="author" x="420" y="1128" font-size="40" text-anchor="middle">DORIAN HALVEY</text>
</svg>
</body>
</html>
```